Corporate PowerPoint design for edtech focused on developing world / emerging markets

I am involved in a edtech startup focused on providing financial literacy for students and young adults in the developing world and emerging markets; currently focus will be on Africa. We are in discussions with the CEO of a bank in S. Africa and would deploy products throughout much of Africa with them. I need a corporate powerpoint that I can use for my customers and for investor presentation. Company name is Tidecrest, which is a surfing term; meant to connotate movement and energy.
Updates

Target Market(s)

target market is two fold - will be selling to execs at banks and telecommunications companies; also need to present to investors.

Industry/Entity Type

Financial

Font styles to use
Sans Serif

Requirements
Must have
• I'd like to have a slide or two that allow me to do columns for things like feature / benefits or just content that doesn't run left to right across the entire powepoint page.
• otherwise, too much color (other than white) uses a ton of ink, so I don't want a full color background e.g. I don't want a blue or green background. I would like to provide some standard corporate info at the bottom - just basics of contact info, url and ability to change them as necessary

```html
<!DOCTYPE html>
<html lang="en">
<head>
<meta charset="utf-8">
<title>Tidecrest – Title Slide</title>
<link href="https://fonts.googleapis.com/css2?family=Roboto+Condensed:wght@300;400;700&display=swap" rel="stylesheet">
<style>
  :root {
    --ocean: #00629a;
    --ocean-tint: #e6f1f7;
    --ocean-wash: #f3f8fb;
    --white: #ffffff;
    --brand-teal: #0d6f8e;
    --footer-bar: #0099cc;
    --text-muted: #2f5f7c;
  }
  * { margin: 0; padding: 0; box-sizing: border-box; }
  html, body {
    width: 1200px;
    height: 900px;
    overflow: hidden;
    background: var(--white);
    font-family: "Roboto Condensed", "Arial Narrow", sans-serif;
  }
  .slide {
    position: relative;
    width: 1200px;
    height: 900px;
    background: var(--white);
  }
  .hero {
    position: absolute;
    left: 0; top: 0;
    width: 1200px;
    height: 702px;
    background: var(--white);
    overflow: hidden;
    border-bottom: 4px solid var(--ocean);
  }
  .hero-decoration {
    position: absolute;
    left: -330px;
    top: -40px;
    width: 705px;
    height: 740px;
    border-radius: 50%;
    background: radial-gradient(circle at 40% 45%, var(--ocean-tint) 0%, var(--ocean-wash) 60%, rgba(255,255,255,0) 72%);
  }
  .title-block {
    position: absolute;
    right: 55px;
    top: 330px;
    width: 440px;
    text-align: right;
  }
  .project-title {
    font-weight: 400;
    font-size: 58px;
    line-height: 1.1;
    letter-spacing: -0.3px;
    color: var(--ocean);
    white-space: nowrap;
  }
  .project-subtext {
    margin-top: 20px;
    font-weight: 400;
    font-size: 21px;
    line-height: 33px;
    color: var(--text-muted);
  }
  .brand-band {
    position: absolute;
    left: 0; top: 706px;
    width: 1200px;
    height: 161px;
    background: var(--white);
  }
  .brand-name {
    position: absolute;
    right: 112px;
    top: 56px;
    font-weight: 700;
    font-size: 56px;
    line-height: 1;
    letter-spacing: 4px;
    text-transform: uppercase;
    color: var(--brand-teal);
  }
  .brand-dot {
    position: absolute;
    right: 33px;
    top: 50px;
    width: 64px;
    height: 64px;
    border-radius: 50%;
    background: var(--brand-teal);
  }
  .footer-bar {
    position: absolute;
    left: 0; top: 867px;
    width: 1200px;
    height: 33px;
    background: var(--footer-bar);
  }
</style>
</head>
<body>
  <main class="slide">
    <section class="hero">
      <div class="hero-decoration" role="img" aria-label="Soft wave motif decoration in pale ocean blue"></div>
      <div class="title-block">
        <h1 class="project-title">Project Title Here</h1>
        <p class="project-subtext">Subtext here Subtext here Subtext here Subtext here Subtext here Subtext here Subtext here Subtext here</p>
      </div>
    </section>
    <section class="brand-band">
      <span class="brand-name">Tidecrest</span>
      <span class="brand-dot" aria-hidden="true"></span>
    </section>
    <div class="footer-bar"></div>
  </main>
</body>
</html>
```